Personal Biography Website for a Professional Game Developer

I'm looking for someone to design a personal biography website for a professional game developer. Look at the attached logos, headshots, and art as examples of the type of style that I'm looking for. This should be an edgy, progressive-style website -- like one you'd expect from a video game website.
I'm also a huge fan of the velmo website... large images for each section with little text.
I've attached the bio text as well (the underlines are just place holders)
Target Market(s)
Venture Capital, Video Game Developers
Number of Pages Required
1 page
Look and feel
Each slider illustrates characteristics of the customer's brand and the style your logo design should communicate.

```html
<!DOCTYPE html>
<html lang="en">
<head>
<meta charset="utf-8">
<title>Marco Delvane – Game Developer</title>
<link href="https://fonts.googleapis.com/css2?family=Montserrat:wght@400;500;700;800;900&display=swap" rel="stylesheet">
<style>
  :root {
    --bg: #000306;
    --ink: #ffffff;
    --cyan: #27c6f2;
    --blue: #1aa4dc;
    --violet: #3b2a6a;
    --red: #e8232f;
    --muted: rgba(255,255,255,0.82);
    --grid: rgba(60,110,140,0.16);
  }
  * { box-sizing: border-box; margin: 0; padding: 0; }
  html, body { width: 876px; height: 1200px; overflow: hidden; background: var(--bg); }
  body { font-family: "Montserrat", Arial, sans-serif; color: var(--ink); position: relative; }

  .grid-bg {
    position: absolute; left: 0; width: 876px;
    background-image:
      linear-gradient(var(--grid) 1px, transparent 1px),
      linear-gradient(90deg, var(--grid) 1px, transparent 1px);
    background-size: 46px 46px;
  }
  .grid-top { top: 0; height: 520px; }
  .grid-mid { top: 555px; height: 510px; opacity: 0.7; }

  .dash { position: absolute; height: 2px; }
  .dash.cyan { background: var(--blue); width: 14px; }
  .dash.red { background: var(--red); width: 34px; }
  .dash.white { background: #fff; width: 11px; }

  /* header */
  .site-header { position: absolute; top: 0; left: 0; width: 876px; height: 70px; z-index: 5; }
  .brand { position: absolute; left: 103px; top: 16px; font-weight: 900; font-size: 26px; letter-spacing: -0.5px; color: var(--cyan); display: flex; align-items: center; gap: 7px; }
  .brand-dot { width: 12px; height: 12px; border-radius: 50%; background: var(--red); }
  .main-nav { position: absolute; top: 24px; left: 443px; display: flex; gap: 0; }
  .main-nav a { color: var(--muted); text-decoration: none; font-size: 9.5px; font-weight: 500; letter-spacing: 0.6px; position: relative; }
  .main-nav a.active { color: #fff; }
  .main-nav a.active::after { content: ""; position: absolute; left: 0; right: 0; bottom: -7px; height: 1.5px; background: linear-gradient(90deg, var(--cyan), var(--red)); }
  .nav-home { margin-right: 45px; } .nav-bio { margin-right: 39px; }

  .social { display: flex; gap: 5px; position: absolute; }
  .social span { width: 26px; height: 26px; border: 1px solid rgba(255,255,255,0.7); border-radius: 50%; display: block; position: relative; }
  .social span::after { content: ""; position: absolute; left: 11px; top: 11px; width: 3px; height: 3px; border-radius: 50%; background: #fff; }
  .social-top { left: 654px; top: 18px; }

  /* hero */
  .hero-photo { position: absolute; left: 430px; top: 0; width: 446px; height: 520px;
    background:
      radial-gradient(ellipse 45% 35% at 55% 25%, rgba(30,140,200,0.75), transparent 70%),
      radial-gradient(ellipse 60% 45% at 50% 60%, rgba(20,70,130,0.55), transparent 75%),
      radial-gradient(ellipse 30% 40% at 95% 40%, rgba(200,30,60,0.5), transparent 70%),
      linear-gradient(180deg, transparent 70%, var(--bg));
  }
  .hero-copy { position: absolute; left: 103px; top: 165px; }
  .hero-first { font-size: 50px; font-weight: 900; line-height: 1; letter-spacing: -1px;
    background: linear-gradient(90deg, var(--blue), var(--violet) 45%, var(--red) 80%);
    -webkit-background-clip: text; background-clip: text; color: transparent; }
  .hero-last { margin-top: 6px; display: block; }
  .hero-role { margin-top: 14px; font-size: 13.5px; font-weight: 400; letter-spacing: 0.3px; color: #fff; }

  .btn-row { position: absolute; display: flex; gap: 11px; }
  .btn { height: 31px; border: 1px solid rgba(255,255,255,0.85); border-radius: 16px; display: flex; align-items: center; justify-content: center; font-size: 9.5px; font-weight: 500; letter-spacing: 0.5px; color: #fff; }
  .btn-contact { width: 110px; } .btn-bio { width: 84px; }
  .hero-btns { left: 103px; top: 325px; }

  /* about */
  .about-photo { position: absolute; left: 0; top: 555px; width: 400px; height: 510px;
    background:
      radial-gradient(ellipse 55% 50% at 40% 45%, rgba(120,25,80,0.7), transparent 75%),
      linear-gradient(120deg, transparent 30%, rgba(30,150,210,0.55) 100%),
      linear-gradient(90deg, rgba(60,40,110,0.5), transparent 95%);
  }
  .about-copy { position: absolute; left: 418px; top: 713px; }
  .about-title { font-size: 24px; font-weight: 700; line-height: 38.5px; letter-spacing: 0.5px; color: #fff; }
  .about-years { margin-top: 10px; font-size: 30px; font-weight: 800; letter-spacing: -0.3px;
    background: linear-gradient(90deg, var(--cyan) 0%, var(--blue) 28%, var(--violet) 42%, var(--red) 75%);
    -webkit-background-clip: text; background-clip: text; color: transparent; }
  .about-btns { left: 416px; top: 900px; }

  /* contact band */
  .contact-band { position: absolute; left: 0; top: 1065px; width: 876px; height: 90px;
    background: linear-gradient(90deg, #22c3f0 0%, #2f5a8e 30%, #4a2358 52%, #8a1c3a 75%, #e8232f 100%); }
  .contact-item { position: absolute; top: 27px; display: flex; align-items: center; gap: 11px; }
  .contact-item svg { width: 37px; height: 37px; }
  .contact-text { font-size: 10px; font-weight: 600; line-height: 17px; letter-spacing: 0.3px; }
  .contact-label { font-size: 9.5px; font-weight: 500; }
  .contact-text .big { font-size: 11px; }
  .divider { position: absolute; top: 10px; width: 1px; height: 70px; background: rgba(255,255,255,0.15); }

  /* footer */
  .site-footer { position: absolute; left: 0; top: 1155px; width: 876px; height: 45px; background: #000; }
  .copyright { position: absolute; left: 103px; top: 17px; font-size: 9.5px; color: var(--muted); letter-spacing: 0.3px; }
  .social-bottom { left: 653px; top: 10px; }
</style>
</head>
<body>
  <div class="grid-bg grid-top"></div>
  <div class="hero-photo" role="img" aria-label="Portrait of the developer lit in blue and red neon"></div>

  <header class="site-header">
    <div class="brand">Delvane <span class="brand-dot"></span></div>
    <nav class="main-nav">
      <a class="nav-home active">HOME</a>
      <a class="nav-bio">BIO</a>
      <a class="nav-contact">CONTACT</a>
    </nav>
    <div class="social social-top" aria-label="Social links">
      <span></span><span></span><span></span><span></span>
    </div>
  </header>

  <span class="dash cyan" style="left:209px;top:83px"></span>
  <span class="dash white" style="left:60px;top:116px"></span>
  <span class="dash cyan" style="left:126px;top:128px"></span>
  <span class="dash red" style="left:37px;top:146px"></span>
  <span class="dash cyan" style="left:393px;top:351px"></span>
  <span class="dash red" style="left:349px;top:372px"></span>
  <span class="dash cyan" style="left:282px;top:386px;width:11px"></span>

  <section class="hero-copy">
    <h1>
      <span class="hero-first">MARCO</span>
      <svg class="hero-last" width="330" height="50" viewBox="0 0 330 50" aria-label="DELVANE">
        <defs>
          <linearGradient id="outlineGrad" x1="0" x2="1" y1="0" y2="0">
            <stop offset="0" stop-color="#27c6f2"/>
            <stop offset="0.5" stop-color="#3b2a6a"/>
            <stop offset="1" stop-color="#e8232f"/>
          </linearGradient>
        </defs>
        <text x="1" y="44" font-family="Montserrat, Arial, sans-serif" font-size="52" font-weight="500" fill="none" stroke="url(#outlineGrad)" stroke-width="1.6" letter-spacing="1">DELVANE</text>
      </svg>
    </h1>
    <p class="hero-role">I Am Professional Game Developer</p>
  </section>
  <div class="btn-row hero-btns">
    <span class="btn btn-contact">CONTACT ME</span>
    <span class="btn btn-bio">READ BIO</span>
  </div>

  <div class="grid-bg grid-mid"></div>
  <div class="about-photo" role="img" aria-label="Close-up portrait of the developer in purple and blue tones"></div>

  <span class="dash cyan" style="left:532px;top:595px"></span>
  <span class="dash white" style="left:384px;top:629px"></span>
  <span class="dash cyan" style="left:450px;top:641px"></span>
  <span class="dash red" style="left:361px;top:659px"></span>
  <span class="dash cyan" style="left:789px;top:939px"></span>
  <span class="dash red" style="left:745px;top:960px"></span>
  <span class="dash cyan" style="left:678px;top:974px;width:11px"></span>

  <section class="about-copy">
    <h2 class="about-title">Passionately Accentuating<br>The Gaming/entertainment<br>Experience For The</h2>
    <p class="about-years">Last 10+ Years.</p>
  </section>
  <div class="btn-row about-btns">
    <span class="btn btn-contact">CONTACT ME</span>
    <span class="btn btn-bio">READ BIO</span>
  </div>

  <section class="contact-band">
    <div class="contact-item" style="left:103px">
      <svg viewBox="0 0 37 37" fill="none" stroke="#fff" stroke-width="1.2">
        <circle cx="18.5" cy="18.5" r="17.5"/>
        <circle cx="17" cy="21" r="8"/>
        <path d="M9 21h16M17 13c-3 3-3 13 0 16M17 13c3 3 3 13 0 16"/>
        <path d="M23 17c-2.5-3-3.5-5-3.5-6.5a3.5 3.5 0 0 1 7 0c0 1.5-1 3.5-3.5 6.5z" fill="#2a7fb5"/>
        <circle cx="23" cy="10.5" r="1"/>
      </svg>
      <div class="contact-text">123, Building Name, Street<br>City, State XY 123456</div>
    </div>
    <span class="divider" style="left:325px"></span>
    <div class="contact-item" style="left:377px">
      <svg viewBox="0 0 37 37" fill="none" stroke="#fff" stroke-width="1.2">
        <circle cx="18.5" cy="18.5" r="17.5"/>
        <path d="M12 11l3-1 2 5-2 1.5c1 2.5 3 4.5 5.5 5.5l1.5-2 5 2-1 3c-7 1-15-7-14-14z"/>
        <path d="M21 10a6 6 0 0 1 6 6M21 13a3 3 0 0 1 3 3"/>
      </svg>
      <div class="contact-text"><span class="contact-label">PHONE</span><br><span class="big">(123) 456 7890</span></div>
    </div>
    <span class="divider" style="left:560px"></span>
    <div class="contact-item" style="left:612px">
      <svg viewBox="0 0 37 37" fill="none" stroke="#fff" stroke-width="1.2">
        <circle cx="18.5" cy="18.5" r="17.5"/>
        <path d="M10 16v11h17V16l-8.5-6z"/>
        <path d="M10 27l7-6h3l7 6M13 18v-5h11v5M15 15h7M15 17h7"/>
      </svg>
      <div class="contact-text"><span class="contact-label">EMAIL</span><br>info@marcodelvane.com</div>
    </div>
  </section>

  <footer class="site-footer">
    <p class="copyright">Copyright 2022. MarcoDelvane. All Rights Reserved</p>
    <div class="social social-bottom" aria-label="Social links">
      <span></span><span></span><span></span><span></span>
    </div>
  </footer>
</body>
</html>
```